Keystone Physical Therapy needs a New website look and update!

New updated look. Most people do not know they can go directly to a physical therapist for care. Cost effective and specialized. Getting back to your life and activity is what we do. What we treat. Your first cost effective provider for pain" for example. We treat children to seniors. Theme should be warm, caring, individualized, respect your time, and cost -effective. Mobile phone ready. Encourage taking action to call and schedule to get back to life, sports, activity.
Add link to send appointment request or contact us now
Add link ( code) for patients to fill out intake form or appointment request. I want to add testimonials for other therapists.
***My current website is "brellowkeypt.net"

```html
<!DOCTYPE html>
<html lang="en">
<head>
<meta charset="utf-8">
<title>Keystone Physical Therapy — Website Pages</title>
<link href="https://fonts.googleapis.com/css2?family=Montserrat:wght@600;700&family=Questrial&display=swap" rel="stylesheet">
<style>
:root{
  --board-light:#4b4b4e;
  --board-dark:#1e1e20;
  --green:#7cc520;
  --green-light:#9bdc3c;
  --teal:#1b97a3;
  --ink:#3a3a3c;
  --muted:#6e6e71;
  --panel:#efefef;
  --line:#d9d9d9;
  --footer:#3d3d40;
  --footer-deep:#2c2c2e;
  --footer-text:#c9c9cc;
  --white:#ffffff;
  --mark:#121212;
}
*{box-sizing:border-box;margin:0;padding:0}
html,body{width:1200px;height:640px;overflow:hidden}
body{font-family:"Questrial",sans-serif;color:var(--ink)}
.board{position:relative;width:1200px;height:640px;overflow:hidden;
  background:radial-gradient(ellipse 70% 80% at 50% 42%,var(--board-light),var(--board-dark))}

/* ---------- shared page chrome ---------- */
.page{position:absolute;background:var(--white);overflow:hidden;font-size:2.8px;line-height:1.4;display:flex;flex-direction:column}
.page--home{left:72px;top:64px;width:256px;height:482px}
.page--providers{left:342px;top:64px;width:264px;height:428px}
.page--needling{left:618px;top:64px;width:254px;height:294px}
.page--contact{left:886px;top:64px;width:242px;height:290px}

.topbar{height:6px;flex:none;background:var(--green);display:flex;justify-content:flex-end;align-items:center;gap:8px;padding:0 14px;color:var(--white);font-size:2.6px}
.site-header{height:22px;flex:none;display:flex;align-items:center;justify-content:space-between;padding:0 12px;background:var(--white);border-bottom:1px solid #f1f1f1}
.brand{display:flex;align-items:center;gap:2px}
.brand-dot{width:11px;height:11px;border-radius:50%;background:var(--green)}
.brand-name{font-family:"Montserrat",sans-serif;font-weight:700;font-size:9px;color:var(--teal);letter-spacing:-.2px}
.site-nav{display:flex;gap:8px;font-family:"Montserrat",sans-serif;font-weight:600;font-size:3.1px;color:var(--teal)}
.site-nav .is-current{color:var(--green)}

.page-title{font-family:"Montserrat",sans-serif;font-weight:700;font-size:4.6px;color:var(--ink);letter-spacing:.2px}

/* ---------- home ---------- */
.hero{height:102px;flex:none;position:relative;
  background:linear-gradient(160deg,#0d2c4a 0%,#1f6ea5 38%,#63b7dd 62%,#123d63 100%)}
.hero-tag{position:absolute;left:22px;font-family:"Montserrat",sans-serif;font-weight:700;line-height:1;padding:1px 2px}
.hero-tag--lead{top:8px;font-size:10.5px;background:var(--green-light);color:#1e3d12}
.hero-tag--sub{top:22px;font-size:8.6px;background:#17607d;color:var(--green-light);font-weight:600}

.about{height:94px;flex:none;background:var(--panel);padding:6px 20px 0;position:relative}
.about .page-title{text-align:center;margin-bottom:3px}
.about p{margin-bottom:2.4px;color:var(--muted);max-width:216px}
.about address{font-style:normal;color:var(--muted);margin-bottom:2px}
.btn-call{position:absolute;right:20px;top:62px;background:var(--green);color:var(--white);font-family:"Montserrat",sans-serif;font-weight:700;font-size:3.6px;padding:3px 5px}

.section-label{height:12px;flex:none;display:flex;align-items:center;justify-content:center;position:relative;background:var(--white)}
.section-label::before{content:"";position:absolute;left:12px;right:12px;top:50%;height:.6px;background:var(--line)}
.section-label span{position:relative;background:var(--ink);color:var(--white);font-family:"Montserrat",sans-serif;font-weight:700;font-size:3.4px;padding:1.2px 4px;letter-spacing:.3px}

.service-grid{height:98px;flex:none;display:grid;grid-template-columns:1fr 1fr 1fr;grid-template-rows:1fr 1fr;gap:1px;background:var(--white)}
.service-tile{position:relative}
.service-tile--massage{background:linear-gradient(135deg,#7bb32a,#a7d060)}
.service-tile--rehab{background:linear-gradient(135deg,#3d8fb0,#bfc9cf)}
.service-tile--gym{background:linear-gradient(135deg,#c9c7c2,#6f6d69)}
.service-tile--therapy{background:linear-gradient(135deg,#e2d8cf,#8b7d72)}
.service-tile--taping{background:linear-gradient(135deg,#f1eeea,#b8aea4)}
.service-tile--training{background:linear-gradient(135deg,#4a4a4a,#7fb64a)}
.service-caption{position:absolute;left:8px;bottom:14px;color:var(--white);font-size:4.4px;letter-spacing:.3px}

.testimonial{height:68px;flex:none;position:relative;text-align:center;padding-top:2px}
.testimonial-avatar{width:13px;height:13px;margin:0 auto 5px;background:linear-gradient(135deg,#c9a98d,#6d5646)}
.testimonial-quote{font-size:3.4px;color:var(--ink);line-height:1.5}
.testimonial-name{font-size:3px;color:var(--teal);margin-top:2px}
.testimonial-dots{margin-top:4px;display:flex;justify-content:center;gap:2px}
.testimonial-dots i{width:1.6px;height:1.6px;border-radius:50%;background:#bbb}
.testimonial-dots i:first-child{background:var(--green)}
.slider-arrow{position:absolute;top:24px;width:6px;height:9px;background:#111;display:flex;align-items:center;justify-content:center}
.slider-arrow--prev{left:0}
.slider-arrow--next{right:0}

/* ---------- footer ---------- */
.site-footer{flex:1;display:flex;flex-direction:column;background:var(--footer);color:var(--footer-text)}
.footer-body{flex:1;display:grid;grid-template-columns:56% 18% 26%;padding:8px 14px 0}
.footer-about p{max-width:90px;font-size:2.4px;margin-top:3px}
.footer-about h4{font-size:3px;color:var(--white);margin-top:6px;font-weight:400}
.footer-heading{font-size:3.2px;color:var(--white);margin-bottom:4px}
.footer-links{list-style:none;font-family:"Montserrat",sans-serif;font-size:2.5px;font-weight:600;color:var(--white);line-height:1.75}
.contact-row{display:flex;gap:2px;margin-bottom:3px;font-size:2.3px}
.contact-icon{width:4.5px;height:4.5px;flex:none;background:var(--green);display:flex;align-items:center;justify-content:center}
.social{display:flex;gap:1.5px;margin-top:2px}
.social i{width:4.5px;height:4.5px;border-radius:50%}
.social i:nth-child(1){background:#3b5a9a}
.social i:nth-child(2){background:#34a9e0}
.social i:nth-child(3){background:#6f7d8c}
.social i:nth-child(4){background:#d44c3b}
.btn-more{display:inline-block;margin-top:5px;background:var(--teal);color:var(--white);font-size:2.4px;padding:1.5px 3px}
.footer-strip{height:7px;flex:none;background:var(--footer-deep);display:flex;align-items:center;justify-content:center;font-size:2.4px;color:var(--footer-text)}
.site-footer .brand-name{font-size:8px}

/* ---------- providers ---------- */
.providers{height:326px;flex:none;padding:14px 14px 0}
.providers .page-title{margin-bottom:4px}
.provider-card{background:var(--panel);display:flex;gap:8px;padding:6px;margin-bottom:6px;overflow:hidden}
.provider-card:nth-of-type(1){height:86px}
.provider-card:nth-of-type(2){height:90px}
.provider-card:nth-of-type(3){height:56px}
.provider-card:nth-of-type(4){height:48px}
.provider-photo{width:38px;height:40px;flex:none}
.provider-photo--one{background:linear-gradient(135deg,#6b4a36,#c49a7c)}
.provider-photo--two{background:linear-gradient(135deg,#d6c4a4,#9a8a73)}
.provider-photo--three{background:linear-gradient(135deg,#a88a71,#4e3b2d)}
.provider-photo--four{background:linear-gradient(135deg,#e0b25a,#8f5b3a)}
.provider-name{font-family:"Montserrat",sans-serif;font-weight:700;font-size:4.6px;color:var(--teal);margin-bottom:2.5px}
.provider-bio p{font-size:2.5px;color:var(--muted);margin-bottom:2px}
.provider-bio ul{font-size:2.5px;color:var(--muted);margin:0 0 2px 8px}

/* ---------- dry needling ---------- */
.needling{height:192px;flex:none;padding:12px 14px 0;position:relative}
.needling .page-title{margin-bottom:6px}
.needling-text{width:112px}
.needling-text h3{font-family:"Montserrat",sans-serif;font-weight:700;font-size:3.9px;color:var(--ink);margin:3px 0 2px}
.needling-text p,.needling-text ul{font-size:2.4px;color:var(--muted)}
.needling-text ul{margin-left:7px}
.needling-wide{width:220px}
.needling-photo{position:absolute;left:130px;top:27px;width:106px;height:68px;background:linear-gradient(135deg,#e4d1c2,#c29c84 55%,#8a6a59)}
.needling-call{font-family:"Montserrat",sans-serif;font-weight:700;font-size:3.5px;color:var(--teal);margin-top:6px;padding-left:10px}

/* ---------- contact ---------- */
.contact{height:192px;flex:none;padding:10px 12px 0;position:relative}
.contact-intro{font-size:2.4px;color:var(--muted);margin:2px 0 6px}
.contact-form{width:118px}
.field-row{display:flex;gap:4px;margin-bottom:3px}
.field{flex:1;height:8px;border:.6px solid #b9e08a;font-size:2.5px;color:var(--muted);padding:2px 3px}
.field--message{height:38px}
.btn-send{display:inline-block;margin-top:6px;background:var(--teal);color:var(--white);font-size:2.6px;padding:2px 5px}
.contact-side{position:absolute;left:160px;top:26px;width:72px}
.map{height:38px;background:linear-gradient(135deg,#e9efe3,#dfe6ee 60%,#cfd9c4)}
.map-caption{font-size:2.2px;color:var(--muted);margin:2px 0 4px}
.info-heading{font-size:2.8px;color:var(--green);font-weight:700;margin:4px 0 3px}
.info-row{display:flex;gap:2px;font-size:2.2px;color:var(--muted);margin-bottom:3px}
.info-icon{width:5px;height:5px;flex:none;background:#111;display:flex;align-items:center;justify-content:center}

/* ---------- brand sign-off ---------- */
.brand-sign{position:absolute;left:862px;top:470px;display:flex;align-items:center;gap:14px}
.brand-sign-square{width:56px;height:56px;background:var(--mark);flex:none}
.brand-sign-name{font-family:"Questrial",sans-serif;font-weight:400;color:var(--mark);line-height:1.1}
.brand-sign-name strong{display:block;font-weight:400;font-size:40px}
.brand-sign-name span{display:block;font-size:17px}
</style>
</head>
<body>
<main class="board">

  <!-- HOME -->
  <section class="page page--home">
    <div class="topbar"><span>303-555-0148</span><span>info@brellowkeypt.net</span></div>
    <header class="site-header">
      <div class="brand"><span class="brand-dot"></span><span class="brand-name">keystone</span></div>
      <nav class="site-nav"><span>HOME</span><span>ABOUT US</span><span>SERVICES</span><span>FORMS</span><span>CONTACT</span></nav>
    </header>
    <div class="hero" role="img" aria-label="Swimmer diving through blue pool water">
      <span class="hero-tag hero-tag--lead">DENVER'S CHOICE</span>
      <span class="hero-tag hero-tag--sub">FOR HEALING AND REHABILITATION</span>
    </div>
    <div class="about">
      <h2 class="page-title">ABOUT US</h2>
      <p>Welcome to Keystone Physical Therapy, southeast Denver's choice for healing and rehabilitation. Our therapist-owned practice is committed to restoring wellness and quality of life with caring, skilled hands for clients of all ages.</p>
      <p>We treat a wide range of injuries and conditions, whether you are recovering from surgery, returning to athletics or simply want to move without pain. We partner with you to reach your goals in a comfortable, well equipped clinic.</p>
      <p>At Keystone PT, our goal is to empower your healing through manual therapy, exercise techniques, postural training and education. Every visit is one on one, so you receive focused care that respects your time and budget.</p>
      <p>Visit us today at our convenient Harlow or Fenwick location to serve you:</p>
      <address>4820 E. Harlow Rd, Suite 3<br>Parkview, CO 80199<br>303-555-0148</address>
      <address>7725 Fenwick Pkwy<br>Parkview, CO 80199<br>303-555-0148</address>
      <span class="btn-call">CALL US TODAY</span>
    </div>
    <div class="section-label"><span>SERVICES</span></div>
    <div class="service-grid">
      <div class="service-tile service-tile--massage" role="img" aria-label="Massage therapy session"><span class="service-caption">MASSAGE THERAPY</span></div>
      <div class="service-tile service-tile--rehab" role="img" aria-label="Patient doing floor rehabilitation exercise"></div>
      <div class="service-tile service-tile--therapy" role="img" aria-label="Therapist working on a patient's shoulder"></div>
      <div class="service-tile service-tile--taping" role="img" aria-label="Kinesiology taping on a knee"></div>
      <div class="service-tile service-tile--gym" role="img" aria-label="Balance training with a therapist"></div>
      <div class="service-tile service-tile--training" role="img" aria-label="Athlete doing agility training on turf"></div>
    </div>
    <div class="section-label"><span>TESTIMONIALS</span></div>
    <div class="testimonial">
      <div class="testimonial-avatar" role="img" aria-label="Patient portrait"></div>
      <p class="testimonial-quote">“The services were great! I would surely recommend this to others.<br>It's been great! I have never felt so relaxed and motivated. Thank you so much!”</p>
      <p class="testimonial-name">Dana Whitfield, Parkview</p>
      <div class="testimonial-dots"><i></i><i></i><i></i><i></i></div>
      <span class="slider-arrow slider-arrow--prev"><svg width="3" height="4" viewBox="0 0 3 4"><path d="M2.5 0 0.5 2 2.5 4Z" fill="#fff"/></svg></span>
      <span class="slider-arrow slider-arrow--next"><svg width="3" height="4" viewBox="0 0 3 4"><path d="M0.5 0 2.5 2 0.5 4Z" fill="#fff"/></svg></span>
    </div>
    <footer class="site-footer">
      <div class="footer-body">
        <div class="footer-about">
          <div class="brand"><span class="brand-dot"></span><span class="brand-name">keystone</span></div>
          <h4>About Us</h4>
          <p>Welcome to Keystone Physical Therapy, southeast Denver's choice for healing and rehabilitation. Our therapist-owned practice is committed to wellness and quality of life for clients of all ages.</p>
          <span class="btn-more">Read More</span>
        </div>
        <div>
          <h4 class="footer-heading">Information</h4>
          <ul class="footer-links"><li>HOME</li><li>ABOUT US</li><li>SERVICES</li><li>INSURANCE</li><li>FORMS</li><li>CONTACT</li></ul>
        </div>
        <div>
          <h4 class="footer-heading">Contact Info</h4>
          <div class="contact-row"><span class="contact-icon"><svg width="3" height="3" viewBox="0 0 10 10"><path d="M5 0C3 0 1.5 1.5 1.5 3.5 1.5 6 5 10 5 10s3.5-4 3.5-6.5C8.5 1.5 7 0 5 0Z" fill="#fff"/></svg></span><span>Harlow Location Clinic<br>4820 E. Harlow Rd, Suite 3<br>Parkview, CO 80199</span></div>
          <div class="contact-row"><span class="contact-icon"><svg width="3" height="3" viewBox="0 0 10 10"><path d="M2 0 4 3 3 4.5C4 6.5 5 7 5.5 7L7 6l3 2-1 2C4 10 0 6 0 1Z" fill="#fff"/></svg></span><span>Phone: 303-555-0148<br>Fax: 303-555-0149</span></div>
          <div class="contact-row"><span class="contact-icon"><svg width="3" height="3" viewBox="0 0 10 10"><path d="M0 2h10v6H0Z M0 2l5 3.5L10 2" fill="none" stroke="#fff" stroke-width="1"/></svg></span><span>Email: info@brellowkeypt.net</span></div>
          <h4 class="footer-heading">Follow Us</h4>
          <div class="social"><i></i><i></i><i></i><i></i></div>
        </div>
      </div>
      <div class="footer-strip">Copyright 2017 - All Right Reserved</div>
    </footer>
  </section>

  <!-- PROVIDERS -->
  <section class="page page--providers">
    <div class="topbar"><span>303-555-0148</span><span>info@brellowkeypt.net</span></div>
    <header class="site-header">
      <div class="brand"><span class="brand-dot"></span><span class="brand-name">keystone</span></div>
      <nav class="site-nav"><span>HOME</span><span class="is-current">ABOUT US</span><span>SERVICES</span><span>FORMS</span><span>CONTACT</span></nav>
    </header>
    <div class="providers">
      <h2 class="page-title">OUR PROVIDERS</h2>
      <article class="provider-card">
        <div class="provider-photo provider-photo--one" role="img" aria-label="Portrait of Claire Hadley"></div>
        <div class="provider-bio">
          <h3 class="provider-name">Claire Hadley, PT, Owner</h3>
          <p>Physical therapist Claire Hadley opened Keystone PT in 2003 to provide personalized, one on one care. She specializes in orthopedic and sports medicine and has over 20 years of clinical experience.</p>
          <p>Claire's areas of special interest include:</p>
          <ul><li>Posture and Biomechanical Alignment</li><li>Manual Therapy</li><li>Shoulder and Lower Extremity Problems</li><li>Core Stabilization</li><li>Pilates</li><li>Custom Orthotics</li></ul>
          <p>Most importantly, Claire is committed to injury prevention and the treatment of young and older athletes alike, from the hip and spine to knee, shoulder and foot.</p>
          <p>Outside the clinic she enjoys skating, hiking and time with family.</p>
        </div>
      </article>
      <article class="provider-card">
        <div class="provider-photo provider-photo--two" role="img" aria-label="Portrait of Renee Calder"></div>
        <div class="provider-bio">
          <h3 class="provider-name">Renee Calder, PT, MS</h3>
          <p>Renee was born, raised and educated in western Montana. Her interest in physical therapy began at an early age through sports, and she earned her degree in Exercise Science before completing graduate school in 2007.</p>
          <p>After graduation, Renee moved to Colorado to pursue her interest in orthopedic and sports rehab. She enjoys working with patients of every age and helping them return to the activities they love most.</p>
          <p>Renee grew up with an active outdoor lifestyle and enjoys skiing, biking, camping and running with her family.</p>
        </div>
      </article>
      <article class="provider-card">
        <div class="provider-photo provider-photo--three" role="img" aria-label="Portrait of Marisa Quinn"></div>
        <div class="provider-bio">
          <h3 class="provider-name">Marisa Quinn, DPT, SCS</h3>
          <p>Marisa earned her Doctorate of Physical Therapy in 2009 and became a Board Certified Sports Clinical Specialist in 2014.</p>
          <p>She has experience with a variety of orthopedic conditions, but has a special interest in young athletes and runners of all ages.</p>
          <p>Marisa has a background in distance running and enjoys trail races and the mountains.</p>
        </div>
      </article>
      <article class="provider-card">
        <div class="provider-photo provider-photo--four" role="img" aria-label="Portrait of Jolene Parrish"></div>
        <div class="provider-bio">
          <h3 class="provider-name">Jolene Parrish, MPT</h3>
          <p>Jolene was born and raised in the Midwest, where she grew up playing softball, volleyball and soccer.</p>
          <p>She attended Midland State University and earned a Master of Physical Therapy in 2001.</p>
          <p>Jolene enjoys helping patients of all ages return to the activities they love.</p>
        </div>
      </article>
    </div>
    <footer class="site-footer">
      <div class="footer-body">
        <div class="footer-about">
          <div class="brand"><span class="brand-dot"></span><span class="brand-name">keystone</span></div>
          <h4>About Us</h4>
          <p>Welcome to Keystone Physical Therapy, southeast Denver's choice for healing and rehabilitation. Our therapist-owned practice is committed to wellness and quality of life for clients of all ages.</p>
          <span class="btn-more">Read More</span>
        </div>
        <div>
          <h4 class="footer-heading">Information</h4>
          <ul class="footer-links"><li>HOME</li><li>ABOUT US</li><li>SERVICES</li><li>INSURANCE</li><li>FORMS</li><li>CONTACT</li></ul>
        </div>
        <div>
          <h4 class="footer-heading">Contact Info</h4>
          <div class="contact-row"><span class="contact-icon"><svg width="3" height="3" viewBox="0 0 10 10"><path d="M5 0C3 0 1.5 1.5 1.5 3.5 1.5 6 5 10 5 10s3.5-4 3.5-6.5C8.5 1.5 7 0 5 0Z" fill="#fff"/></svg></span><span>Harlow Location Clinic<br>4820 E. Harlow Rd, Suite 3<br>Parkview, CO 80199</span></div>
          <div class="contact-row"><span class="contact-icon"><svg width="3" height="3" viewBox="0 0 10 10"><path d="M2 0 4 3 3 4.5C4 6.5 5 7 5.5 7L7 6l3 2-1 2C4 10 0 6 0 1Z" fill="#fff"/></svg></span><span>Phone: 303-555-0148<br>Fax: 303-555-0149</span></div>
          <div class="contact-row"><span class="contact-icon"><svg width="3" height="3" viewBox="0 0 10 10"><path d="M0 2h10v6H0Z M0 2l5 3.5L10 2" fill="none" stroke="#fff" stroke-width="1"/></svg></span><span>Email: info@brellowkeypt.net</span></div>
          <h4 class="footer-heading">Follow Us</h4>
          <div class="social"><i></i><i></i><i></i><i></i></div>
        </div>
      </div>
      <div class="footer-strip">Copyright 2017 - All Right Reserved</div>
    </footer>
  </section>

  <!-- DRY NEEDLING -->
  <section class="page page--needling">
    <div class="topbar"><span>303-555-0148</span><span>info@brellowkeypt.net</span></div>
    <header class="site-header">
      <div class="brand"><span class="brand-dot"></span><span class="brand-name">keystone</span></div>
      <nav class="site-nav"><span>HOME</span><span class="is-current">ABOUT US</span><span>SERVICES</span><span>FORMS</span><span>CONTACT</span></nav>
    </header>
    <div class="needling">
      <h2 class="page-title">DRY NEEDLING</h2>
      <div class="needling-text">
        <h3>What is Trigger Point Dry Needling?</h3>
        <p>It is an extremely effective technique using a very fine, solid filament needle to release tight or shortened areas in your muscles. It is called dry needling because no solution is injected. The needle is used to release a trigger point, restoring motion and easing pain.</p>
        <h3>At KPT we use TPDN daily to :</h3>
        <ul><li>Speed healing time</li><li>Induce a healing response in the tissue</li><li>Restore tissue length</li><li>Reduce muscle tension and pain</li><li>Increase mobility</li><li>Get people back to sport and exercise ASAP</li></ul>
      </div>
      <div class="needling-text needling-wide">
        <h3>What types of Conditions does TPDN assist?</h3>
        <ul><li>Neck, back, hip, knee, shoulder pain</li><li>Achilles tendinitis and plantar fasciitis</li><li>Muscle strains/ sprains</li><li>Headaches</li><li>Athletic performance, overuse</li></ul>
        <h3>Does the needle hurt?</h3>
        <p>Because acupuncture needles are very fine and solid, they do not hurt like injection needles. You may feel a twitch, deep ache, soreness and cramping. Any discomfort is short and worth the relief it provides.</p>
        <h3>Is Trigger Point Dry Needling &nbsp;Acupuncture?</h3>
        <p>No. TPDN is based on western medical research and principles. Dry needling is based on the current understanding of neurophysiology and functional anatomy.</p>
        <p class="needling-call">For more information please call 303-555-0148</p>
      </div>
      <div class="needling-photo" role="img" aria-label="Fine needles placed in a patient's shoulder"></div>
    </div>
    <footer class="site-footer">
      <div class="footer-body">
        <div class="footer-about">
          <div class="brand"><span class="brand-dot"></span><span class="brand-name">keystone</span></div>
          <h4>About Us</h4>
          <p>Welcome to Keystone Physical Therapy, southeast Denver's choice for healing and rehabilitation. Our therapist-owned practice is committed to wellness and quality of life for clients of all ages.</p>
          <span class="btn-more">Read More</span>
        </div>
        <div>
          <h4 class="footer-heading">Information</h4>
          <ul class="footer-links"><li>HOME</li><li>ABOUT US</li><li>SERVICES</li><li>INSURANCE</li><li>FORMS</li><li>CONTACT</li></ul>
        </div>
        <div>
          <h4 class="footer-heading">Contact Info</h4>
          <div class="contact-row"><span class="contact-icon"><svg width="3" height="3" viewBox="0 0 10 10"><path d="M5 0C3 0 1.5 1.5 1.5 3.5 1.5 6 5 10 5 10s3.5-4 3.5-6.5C8.5 1.5 7 0 5 0Z" fill="#fff"/></svg></span><span>Harlow Location Clinic<br>4820 E. Harlow Rd, Suite 3<br>Parkview, CO 80199</span></div>
          <div class="contact-row"><span class="contact-icon"><svg width="3" height="3" viewBox="0 0 10 10"><path d="M2 0 4 3 3 4.5C4 6.5 5 7 5.5 7L7 6l3 2-1 2C4 10 0 6 0 1Z" fill="#fff"/></svg></span><span>Phone: 303-555-0148<br>Fax: 303-555-0149</span></div>
          <div class="contact-row"><span class="contact-icon"><svg width="3" height="3" viewBox="0 0 10 10"><path d="M0 2h10v6H0Z M0 2l5 3.5L10 2" fill="none" stroke="#fff" stroke-width="1"/></svg></span><span>Email: info@brellowkeypt.net</span></div>
          <h4 class="footer-heading">Follow Us</h4>
          <div class="social"><i></i><i></i><i></i><i></i></div>
        </div>
      </div>
      <div class="footer-strip">Copyright 2017 - All Right Reserved</div>
    </footer>
  </section>

  <!-- CONTACT -->
  <section class="page page--contact">
    <div class="topbar"><span>303-555-0148</span><span>info@brellowkeypt.net</span></div>
    <header class="site-header">
      <div class="brand"><span class="brand-dot"></span><span class="brand-name">keystone</span></div>
      <nav class="site-nav"><span>HOME</span><span>ABOUT US</span><span>SERVICES</span><span>FORMS</span><span class="is-current">CONTACT</span></nav>
    </header>
    <div class="contact">
      <h2 class="page-title">CONTACT US</h2>
      <p class="contact-intro">For feedback or to make an appointment or request more information:</p>
      <form class="contact-form">
        <div class="field-row"><span class="field">NAME</span><span class="field">PHONE</span></div>
        <div class="field-row"><span class="field">EMAIL</span><span class="field">SUBJECT</span></div>
        <div class="field-row"><span class="field field--message">MESSAGE</span></div>
        <span class="btn-send">SEND</span>
      </form>
      <aside class="contact-side">
        <div class="map" role="img" aria-label="Street map of the Harlow clinic"></div>
        <p class="map-caption">Harlow Location Clinic<br>4820 E. Harlow Rd, Suite 3, Parkview, CO 80199</p>
        <div class="map" role="img" aria-label="Street map of the Fenwick clinic"></div>
        <p class="map-caption">Fenwick<br>7725 Fenwick Pkwy, Parkview, CO 80199<br>Located in the Fenwick Fieldhouse</p>
        <h4 class="info-heading">INFORMATION</h4>
        <div class="info-row"><span class="info-icon"><svg width="3" height="3" viewBox="0 0 10 10"><path d="M5 0C3 0 1.5 1.5 1.5 3.5 1.5 6 5 10 5 10s3.5-4 3.5-6.5C8.5 1.5 7 0 5 0Z" fill="#fff"/></svg></span><span>Keystone Physical Therapy<br>P.O. Box 4417, Parkview, CO 80199</span></div>
        <div class="info-row"><span class="info-icon"><svg width="3" height="3" viewBox="0 0 10 10"><path d="M2 0 4 3 3 4.5C4 6.5 5 7 5.5 7L7 6l3 2-1 2C4 10 0 6 0 1Z" fill="#fff"/></svg></span><span>Phone: 303-555-0148<br>Fax: 303-555-0149</span></div>
        <div class="info-row"><span class="info-icon"><svg width="3" height="3" viewBox="0 0 10 10"><path d="M0 2h10v6H0Z M0 2l5 3.5L10 2" fill="none" stroke="#fff" stroke-width="1"/></svg></span><span>Email: info@brellowkeypt.net</span></div>
      </aside>
    </div>
    <footer class="site-footer">
      <div class="footer-body">
        <div class="footer-about">
          <div class="brand"><span class="brand-dot"></span><span class="brand-name">keystone</span></div>
          <h4>About Us</h4>
          <p>Welcome to Keystone Physical Therapy, southeast Denver's choice for healing and rehabilitation. Our therapist-owned practice is committed to wellness and quality of life for clients of all ages.</p>
          <span class="btn-more">Read More</span>
        </div>
        <div>
          <h4 class="footer-heading">Information</h4>
          <ul class="footer-links"><li>HOME</li><li>ABOUT US</li><li>SERVICES</li><li>INSURANCE</li><li>FORMS</li><li>CONTACT</li></ul>
        </div>
        <div>
          <h4 class="footer-heading">Contact Info</h4>
          <div class="contact-row"><span class="contact-icon"><svg width="3" height="3" viewBox="0 0 10 10"><path d="M5 0C3 0 1.5 1.5 1.5 3.5 1.5 6 5 10 5 10s3.5-4 3.5-6.5C8.5 1.5 7 0 5 0Z" fill="#fff"/></svg></span><span>Harlow Location Clinic<br>4820 E. Harlow Rd, Suite 3<br>Parkview, CO 80199</span></div>
          <div class="contact-row"><span class="contact-icon"><svg width="3" height="3" viewBox="0 0 10 10"><path d="M2 0 4 3 3 4.5C4 6.5 5 7 5.5 7L7 6l3 2-1 2C4 10 0 6 0 1Z" fill="#fff"/></svg></span><span>Phone: 303-555-0148<br>Fax: 303-555-0149</span></div>
          <div class="contact-row"><span class="contact-icon"><svg width="3" height="3" viewBox="0 0 10 10"><path d="M0 2h10v6H0Z M0 2l5 3.5L10 2" fill="none" stroke="#fff" stroke-width="1"/></svg></span><span>Email: info@brellowkeypt.net</span></div>
          <h4 class="footer-heading">Follow Us</h4>
          <div class="social"><i></i><i></i><i></i><i></i></div>
        </div>
      </div>
      <div class="footer-strip">Copyright 2017 - All Right Reserved</div>
    </footer>
  </section>

  <!-- BRAND SIGN-OFF -->
  <div class="brand-sign">
    <span class="brand-sign-square"></span>
    <p class="brand-sign-name"><strong>Keystone</strong><span>Physical Therapy, PC</span></p>
  </div>

</main>
</body>
</html>
```